Harborlight Capital Estates business card

We are a real estate advisory and investment company. We are specialized in assisting high networth individuals to invest in real estate overseas. We deliver a very personalized service, anticipating all the potential challenges an investor can face, and making it easy and safe for them. We also co-invest with our clients, assuring them that each project will be looked after as it is our own, and at the same time giving them the extra booth on confidence to invest.

We need a business card design. The business card must have a very premium, high-end look, reflecting principles like "commitment", "trust" and "timeless (but contemporary)". We look for long term relationships with our clients, and we grow with their referrals. We are all about conquering the confidence of the clients by always delivering above the expectations performance.

Target Market(s)

High net worth individuals.

Industry/Entity Type

Real Estate

Contact Information for Business Card

Please consider places on the business card for:

Name
Function (bellow name in smaller size text)

Mobile phone
E-mail
Skype ID
WeChat ID

Adress (3 lines)

Also include the following locations references:
PORTUGAL * DUBAI * HONG KONG

Website: www.hcestates-example.com

Requirements
Must have
• Company Logo

```html
<!DOCTYPE html>
<html lang="en">
<head>
<meta charset="utf-8">
<title>Harborlight Capital Estates — Business Card</title>
<link rel="stylesheet" href="https://fonts.googleapis.com/css2?family=Montserrat:wght@400;500;600&family=Cormorant+Garamond:wght@500&display=swap">
<style>
  :root{
    --stage:#2b2b2d;
    --card:#050505;
    --accent:#29abe2;
    --paper:#ffffff;
    --text:#f2f2f2;
    --rule:#cfcfcf;
  }
  *{margin:0;padding:0;box-sizing:border-box}
  html,body{width:1200px;height:900px;overflow:hidden;background:var(--stage)}
  .canvas{position:relative;width:1200px;height:900px}
  .card{position:absolute;width:560px;height:320px;background:var(--card);border-radius:22px;overflow:hidden;
        box-shadow:0 18px 40px rgba(0,0,0,.45);font-family:"Montserrat",sans-serif;color:var(--text)}
  .card-front{left:70px;top:80px}
  .card-back{left:570px;top:500px}
  .card-shapes{position:absolute;inset:0;width:100%;height:100%}

  /* front */
  .front-brand{position:absolute;left:0;right:0;top:92px;text-align:center;color:var(--accent);
               font-weight:500;font-size:30px;letter-spacing:5px;line-height:1.25;text-transform:uppercase}
  .locations{position:absolute;left:50%;top:200px;transform:translateX(-50%);display:flex;
             border:2px solid var(--accent);padding:3px}
  .locations span{font-weight:600;font-size:13px;letter-spacing:1px;color:var(--paper);
                  padding:3px 9px;border-left:2px solid var(--accent)}
  .locations span:first-child{border-left:none}
  .front-web{position:absolute;left:26px;bottom:10px;font-size:15px;color:var(--paper);letter-spacing:.5px}

  /* back */
  .back-brand{position:absolute;left:32px;top:92px;color:var(--accent);font-weight:500;
              font-size:21px;letter-spacing:3px;line-height:1.3;text-transform:uppercase}
  .holder{position:absolute;right:34px;top:40px;text-align:right}
  .holder-name{font-family:"Cormorant Garamond",serif;font-weight:500;color:var(--accent);
               font-size:22px;letter-spacing:1px;text-transform:uppercase}
  .holder-role{font-size:12px;color:var(--text)}
  .rule-long{position:absolute;left:200px;right:34px;top:94px;height:1px;background:var(--rule)}
  .rule-short{position:absolute;left:32px;width:220px;top:182px;height:1px;background:var(--rule)}
  .address{position:absolute;left:32px;top:190px;font-size:13px;line-height:1.3}
  .contacts{position:absolute;left:32px;top:245px;list-style:none;font-size:13px;line-height:1.35}
  .contacts li{display:flex;align-items:center;gap:8px}
  .contacts svg{width:11px;height:11px;fill:var(--accent)}
</style>
</head>
<body>
<main class="canvas">

  <section class="card card-front" aria-label="Card front">
    <svg class="card-shapes" viewBox="0 0 560 320" aria-hidden="true">
      <polygon points="0,272 262,272 290,288 560,288 560,300 0,300" fill="var(--paper)" opacity="0"/>
      <polygon points="262,283 560,283 560,294 270,294" fill="var(--paper)"/>
      <polygon points="0,268 250,268 282,288 282,320 0,320" fill="var(--accent)"/>
    </svg>
    <div class="front-brand">Harborlight<br>Capital Estates</div>
    <div class="locations">
      <span>PORTUGAL</span><span>DUBAI</span><span>HONG KONG</span>
    </div>
    <div class="front-web">www.hcestates-example.com</div>
  </section>

  <section class="card card-back" aria-label="Card back">
    <svg class="card-shapes" viewBox="0 0 560 320" aria-hidden="true">
      <polygon points="362,196 560,196 560,258 340,258" fill="var(--accent)"/>
      <polygon points="0,306 318,306 336,266 348,266 328,314 0,314" fill="var(--paper)"/>
    </svg>
    <div class="holder">
      <div class="holder-name">Marcus Ellery</div>
      <div class="holder-role">Function</div>
    </div>
    <div class="rule-long"></div>
    <div class="back-brand">Harborlight<br>Capital Estates</div>
    <div class="rule-short"></div>
    <div class="address">PO Box 48210<br>Harbor Quay<br>NSW 2000</div>
    <ul class="contacts">
      <li><svg viewBox="0 0 24 24"><path d="M6.6 10.8a15.1 15.1 0 0 0 6.6 6.6l2.2-2.2a1 1 0 0 1 1-.25 11.4 11.4 0 0 0 3.6.57 1 1 0 0 1 1 1V20a1 1 0 0 1-1 1A17 17 0 0 1 3 4a1 1 0 0 1 1-1h3.5a1 1 0 0 1 1 1c0 1.25.2 2.45.57 3.57a1 1 0 0 1-.25 1z"/></svg>+330 2450-5172</li>
      <li><svg viewBox="0 0 24 24"><path d="M2 5h20v14H2zm2 2v.5l8 5 8-5V7zm0 2.8V17h16V9.8l-8 5z"/></svg>info@hcestates-example.com</li>
      <li><svg viewBox="0 0 24 24"><path d="M12 2a10 10 0 1 0 0 20 10 10 0 0 0 0-20zm6.9 6h-3a15 15 0 0 0-1.3-3.9A8 8 0 0 1 18.9 8zM12 4c.8 1.1 1.5 2.5 1.9 4h-3.8c.4-1.5 1.1-2.9 1.9-4zM4.3 14a8 8 0 0 1 0-4h3.4a16 16 0 0 0 0 4zm.8 2h3a15 15 0 0 0 1.3 3.9A8 8 0 0 1 5.1 16zm3-8h-3a8 8 0 0 1 4.3-3.9A15 15 0 0 0 8.1 8zM12 20c-.8-1.1-1.5-2.5-1.9-4h3.8c-.4 1.5-1.1 2.9-1.9 4zm2.3-6H9.7a14 14 0 0 1 0-4h4.6a14 14 0 0 1 0 4zm.3 5.9a15 15 0 0 0 1.3-3.9h3a8 8 0 0 1-4.3 3.9zm1.7-5.9a16 16 0 0 0 0-4h3.4a8 8 0 0 1 0 4z"/></svg>www.hcestates-example.com</li>
    </ul>
  </section>

</main>
</body>
</html>
```